Premium Nail Dip Powder Label Design

We need a label design for a 2 ounce jar in which we will be selling our new product line of dip powder to nail salons. For reference, please see competitors' products that are currently selling in the market. The label size is 16cm long by 2.5cm wide. We have a logo design that is attached - the "drop" should be in shiny gold (metallic). This label will wrap around the round jar and the first half will be the "front" and the second half will be the "back". Please see the attached writing that will be required for the second half, or "back" part of the label.

Target Market(s)

Retail Nail Salons in the US

Font styles to use
Sans Serif

Colors

Designer to choose colors to be used in the design.

Requirements
Must have
• "RWT" logo with the "drop" in shiny/metallic gold to match the shiny gold lid that we will have for it. The words "Premium Dip Powder". The size "2 oz". The wording for the second half, or "back" part of the label attached should be in black color with the size adjusted to fit the label size.
Nice to have
• different designs of fonts and sizes and colors for "Premium Dip Powder" which should be on the "front" of the label under our logo.

```html
<!DOCTYPE html>
<html lang="en">
<head>
<meta charset="utf-8">
<title>RWT Premium Dip Powder – Jar Label</title>
<link href="https://fonts.googleapis.com/css2?family=Arimo:wght@400;700&family=Pinyon+Script&display=swap" rel="stylesheet">
<style>
  :root {
    --stage: #1f1f1f;
    --label: #ffffff;
    --ink: #1a1a1a;
    --rule: #3a3a3a;
    --gold-deep: #c98a1e;
    --gold-mid: #d9a92c;
    --gold-light: #f7ec8e;
    --gold-brand: #d8a823;
  }
  * { box-sizing: border-box; margin: 0; padding: 0; }
  html, body { width: 1113px; height: 1200px; overflow: hidden; }
  body {
    background: var(--stage);
    font-family: "Arimo", Arial, sans-serif;
    color: var(--ink);
    position: relative;
  }
  .jar-label {
    position: absolute;
    left: 24px;
    top: 518px;
    width: 1065px;
    height: 165px;
    background: var(--label);
  }
  .gold-band {
    position: absolute;
    left: 0;
    width: 100%;
    background: linear-gradient(90deg,
      var(--gold-mid) 0%, var(--gold-light) 14%, var(--gold-mid) 28%,
      var(--gold-deep) 40%, var(--gold-light) 52%, var(--gold-mid) 64%,
      var(--gold-light) 78%, var(--gold-mid) 90%, var(--gold-deep) 100%);
  }
  .gold-band--top { top: 12px; height: 15px; }
  .gold-band--bottom { top: 137px; height: 15px; }

  .pro-notice {
    position: absolute;
    left: 172px;
    top: 34px;
    font-size: 10px;
    font-weight: 700;
  }
  .info-box {
    position: absolute;
    border: 1px solid var(--rule);
    text-align: center;
    font-size: 8.5px;
    line-height: 1.3;
  }
  .info-box strong { font-size: 9.5px; font-weight: 700; }
  .caution { left: 26px; top: 47px; width: 229px; height: 43px; padding-top: 3px; }
  .ingredients { left: 278px; top: 47px; width: 217px; height: 61px; padding: 2px 8px 0; }
  .maker {
    position: absolute;
    left: 48px;
    top: 96px;
    width: 230px;
    text-align: center;
    font-size: 9.5px;
    line-height: 1.3;
  }
  .maker strong { font-weight: 700; }

  .front-panel {
    position: absolute;
    left: 680px;
    top: 30px;
    width: 275px;
    text-align: center;
  }
  .brand-mark {
    display: inline-flex;
    align-items: center;
    gap: 5px;
    font-size: 36px;
    font-weight: 700;
    line-height: 1;
    color: var(--gold-brand);
    letter-spacing: 1px;
  }
  .brand-dot {
    width: 12px;
    height: 12px;
    border-radius: 50%;
    background: var(--gold-brand);
  }
  .product-name {
    font-family: "Pinyon Script", cursive;
    font-size: 27px;
    line-height: 1;
    margin-top: 6px;
  }
  .product-size {
    font-size: 14px;
    line-height: 1;
    margin-top: -2px;
  }
</style>
</head>
<body>
  <section class="jar-label">
    <div class="gold-band gold-band--top"></div>

    <p class="pro-notice">For Use By Nail Professionals Only</p>

    <div class="info-box caution">
      <strong>CAUTION:&nbsp; KEEP OUT OF REACH OF CHILDREN.</strong><br>
      Keep away from heat, humidity and sunlight.<br>
      Discontinue use if sensitivity or irritation occurs.
    </div>

    <div class="info-box ingredients">
      <strong>INGREDIENTS:</strong><br>
      Polyethylmethacrylate, Acrylates Copolymer,
      Benzoyl Peroxide and PEG-12 Dimethicone.
      May also contain various coloring agents and glitters.
    </div>

    <p class="maker">
      <strong>Manufactured Exclusively For:</strong><br>
      Blue Harbor Trading, Inc., USA<br>
      www.blueharbortrading.com
    </p>

    <div class="front-panel">
      <div class="brand-mark">RWT<span class="brand-dot"></span></div>
      <p class="product-name">Premium Dip Powder</p>
      <p class="product-size">2 oz</p>
    </div>

    <div class="gold-band gold-band--bottom"></div>
  </section>
</body>
</html>
```